eBook and paperback cover

I need an eBook cover (planned release via Brindlemark and Qualto) and subsequently also a paperback cover (planned release via Telpuni), which looks appealing even in black and white and small format and reflects the following novel content.

The text consists of about 420 standard pages - how many pages the paperback will have in the end, I cannot say at the moment. Thus the cover should be designed in a way that the thickness of the spine can be adjusted by me if necessary. Please also take necessary crop margins into account with regard to the paperback cover.

Book title: Das Fenster, hinter dem kein Licht brennt
Author: Marlene Quistorf
Untertitel: Roman

General information about the content:

The core theme of the story is jealousy and self-identity: Emma, the main character (= 18 years old, long brown hair, brown eyes, pretty), finds out that her sister Céline (= 18 years old, dark-blond hair, brown-green eyes, thin) that is at the same age, lives the life of her dreams. Later she finds out, that her sisters life is not the way she imagined in the beginning – nothing is, what it seems to be.

Other relevant characters are Ferdinand (father of Emma and Céline), his friend and business partner Karl) and Emmas mother, the maid (Ekaterina).

The novel takes place in Vienna (Austria).

Blurb:

When Emma surprisingly finds out that she is adopted and is supposed to be the daughter of the wealthy Austrian Ferdinand and his maid Ekaterina, she scents a chance to escape her miserable life. Full of hope she travels to Vienna, where she experiences a bitter disappointment: Her father is anything but happy to see her, Ekaterina in not there and her half-sister Céline, who is the same age, seems to be living the life of her dreams.

But it was to get even worse: Back at home, Emma gradually slipped away from everything she had clung to in life. In her desperation, she is angry at her father, whom she blames for her fate, and jealous of her half-sister. In her quest for retribution, Emma becomes entangled in a maelstrom of intrigue that is set to change her life forever and put her understanding of justice to the test.

Target Market(s)

Women (age 28-65)

Colors
d3a5cc
b8a6cd
eea4c8
f59195
fabb94
fbc994
85acd3
fbf289

Requirements
Must have
• ebook cover (brindlemark standard size) and paperback cover (DIN A5)
Nice to have
• Colors as selected below (but please not all of them)

```html
<!DOCTYPE html>
<html lang="de">
<head>
<meta charset="utf-8">
<title>Das Fenster, hinter dem kein Licht brennt – Umschlag</title>
<link rel="stylesheet" href="https://fonts.googleapis.com/css2?family=Cinzel:wght@400&family=Open+Sans:wght@400;700&display=swap">
<style>
  :root {
    --page: #ffffff;
    --panel-blue: #9db9db;
    --title-blue: #7ea3cf;
    --band-blue: rgba(133, 172, 211, 0.85);
    --mist-top: #f5f5f4;
    --mist-mid: #e2dedb;
    --trunk-grey: #cfc7c2;
    --ground-light: #b49a86;
    --ground-dark: #6f5140;
    --spine-ink: #3b3734;
    --white: #ffffff;
    --isbn-ink: #8a8a8a;
  }
  html, body {
    margin: 0;
    width: 1200px;
    height: 907px;
    overflow: hidden;
    background: var(--page);
  }
  .cover-spread {
    position: absolute;
    left: 50px;
    top: 69px;
    width: 1100px;
    height: 768px;
    overflow: hidden;
  }
  .back-panel {
    position: absolute;
    left: 0; top: 0;
    width: 288px; height: 768px;
    box-sizing: border-box;
    padding: 66px 22px 0 54px;
    display: flex;
    flex-direction: column;
    align-items: flex-start;
    background: linear-gradient(180deg, var(--panel-blue) 0%, var(--panel-blue) 62%, #93acc9 82%, #8ea4bd 100%);
    z-index: 2;
  }
  .back-title {
    margin: 0;
    width: 212px;
    font-family: "Cinzel", serif;
    font-weight: 400;
    font-size: 22px;
    line-height: 25px;
    color: var(--white);
  }
  .back-rule {
    flex: none;
    width: 78px; height: 2px;
    margin: 14px 0 14px;
    background: var(--white);
  }
  .blurb {
    width: 208px;
    font-family: "Open Sans", sans-serif;
    font-size: 11.4px;
    line-height: 18.2px;
    color: var(--white);
  }
  .blurb p { margin: 0 0 10px; }
  .blurb strong { font-weight: 700; }
  .scene-photo {
    position: absolute;
    left: 288px; top: 0;
    width: 812px; height: 768px;
    background:
      linear-gradient(90deg, transparent 0%, rgba(200,190,184,0.35) 33%, rgba(180,170,165,0.45) 36%, transparent 40%, transparent 100%),
      linear-gradient(180deg, var(--mist-top) 0%, var(--mist-mid) 45%, var(--trunk-grey) 62%, var(--ground-light) 76%, var(--ground-dark) 100%);
  }
  .isbn-box {
    position: absolute;
    left: 317px; top: 640px;
    width: 169px; height: 87px;
    background: var(--white);
    display: flex; align-items: center; justify-content: center;
    font-family: "Open Sans", sans-serif;
    font-size: 10px;
    color: var(--isbn-ink);
    z-index: 3;
  }
  .spine-title, .spine-author {
    position: absolute;
    writing-mode: vertical-rl;
    font-weight: 400;
    color: var(--spine-ink);
    margin: 0;
  }
  .spine-title {
    left: 538px; top: 44px;
    font-family: "Cinzel", serif;
    font-size: 21px;
    line-height: 26px;
  }
  .spine-author {
    left: 544px; top: 428px;
    font-family: "Open Sans", sans-serif;
    font-size: 19px;
    line-height: 26px;
  }
  .front-title {
    position: absolute;
    left: 590px; top: 56px;
    width: 510px;
    margin: 0;
    text-align: center;
    font-family: "Cinzel", serif;
    font-weight: 400;
    font-size: 42px;
    line-height: 48px;
    color: var(--title-blue);
  }
  .author-band {
    position: absolute;
    left: 488px; top: 673px;
    width: 612px; height: 41px;
    background: var(--band-blue);
  }
  .author-name {
    position: absolute;
    left: 590px; top: 673px;
    width: 510px; height: 41px;
    margin: 0;
    text-align: center;
    font-family: "Open Sans", sans-serif;
    font-weight: 400;
    font-size: 30px;
    line-height: 41px;
    color: var(--white);
  }
</style>
</head>
<body>
  <main class="cover-spread">
    <div class="scene-photo" role="img" aria-label="Foggy forest with bare trees and a reddish-brown earth path; a young woman with long brown hair sits on the ground with her back turned, another girl sits hugging her knees on the back cover"></div>

    <section class="back-panel">
      <h2 class="back-title">DAS FENSTER,<br>HINTER DEM KEIN<br>LICHT BRENNT</h2>
      <div class="back-rule"></div>
      <div class="blurb">
        <p><strong>When Emma surprisingly finds out that she is adopted and is supposed to be the daughter of the wealthy Austrian Ferdinand and his maid Ekaterina, she scents a chance to escape her miserable life.</strong> Full of hope she travels to Vienna, where she experiences a bitter disappointment: Her father is anything but happy to see her, Ekaterina in not there and her half-sister Céline, who is the same age, seems to be living the life of her dreams.</p>
        <p><strong>But it was to get even worse:</strong> Back at home, Emma gradually slipped away from everything she had clung to in life. In her desperation, she is angry at her father, whom she blames for her fate, and jealous of her half-sister. In her quest for retribution, Emma becomes entangled in a maelstrom of intrigue that is set to change her life forever and put her understanding of justice to the test.</p>
      </div>
    </section>

    <div class="isbn-box">ISBN</div>

    <p class="spine-title">DAS FENSTER, HINTER DEM<br>KEIN LICHT BRENNT</p>
    <p class="spine-author">MARLENE QUISTORF</p>

    <h1 class="front-title">DAS FENSTER,<br>HINTER DEM<br>KEIN LICHT BRENNT</h1>

    <div class="author-band"></div>
    <p class="author-name">MARLENE QUISTORF</p>
  </main>
</body>
</html>
```